BRIGHTDESK - Remote Tech Support Site

We are looking for a new very responsive and simple website for our brand Brightdesk.com - a remote technical support company.

This company supports customers Globally in different countries throughout Eur/ North America / South America / Asia etc (please keep this in mind and integrate into the idea).

Its important to us that the design is very explanatory, the customer should easily be able to figure out that we provide computer support right away ... I like one page responsive type designs as well without a bunch of menu items

Here are some similar sites we like - but still looking for a unique design that fits out brand "brightdesk" - I have upload also some layouts i like (but the designs are not important just the layouts), youll see it includes consumer business etc which is important.

VOLM.COM - I love how clean it is - nice and white easy to see everything

PLUMWIRE247.COM - also nice the layout and responsive one page design makes it easy to use

corvalfix.com - similar to plumwire design as well - you can get the idea im looking for between the two

You will notice those examples are much different then the attachments I added - again this is more of an idea for possible layouts .. attached is also the logo - could inspire color scheme / blue white black etc

Target Market(s)

Home consumers without computer knowledge , older age 45-65, small medium business ... computer repair - slow computers

Industry/Entity Type

Computer Repair

Logo Text

Brightdesk

Coding

Coded - Design and coding required

Number of Pages Required

1 page

Font styles to use
Sans Serif
Other font styles liked:
• your choice responsive

Colors

Designer to choose colors to be used in the design.

Requirements
Must have
• Clean - responsive - professional design - the name says it all - brightdesk
• CALL TO ACTIONS FOR "Get Help Now!" / "Learn More" etc
Nice to have
• We are looking for a new very responsive and simple website for our brand Brightdesk.com - a remote technical support company.
• This company supports customers Globally in different countries throughout Eur/ North America / South America / Asia etc (please keep this in mind and integrate into the idea).
• Its important to us that the design is very explanatory, the customer should easily be able to figure out that we provide computer support right away ... I like one page responsive type designs as well without a bunch of menu items
• Here are some similar sites we like - but still looking for a unique design that fits out brand "brightdesk" - I have upload also some layouts i like (but the designs are not important just the layouts), youll see it includes consumer business etc which is important.
• VOLM.COM - I love how clean it is - nice and white easy to see everything
• PLUMWIRE247.COM - also nice the layout and responsive one page design makes it easy to use
• corvalfix.com - similar to plumwire design as well - you can get the idea im looking for between the two
Should not have
• dark, packed page - bad small font -

```html
<!DOCTYPE html>
<html lang="en">
<head>
<meta charset="utf-8">
<title>Brightdesk – Remote Tech Support</title>
<link rel="stylesheet" href="https://fonts.googleapis.com/css2?family=Roboto:wght@300;400;500;700&family=Roboto+Condensed:wght@400;700&display=swap">
<style>
:root{
  --blue:#1e88e5;
  --blue-bright:#2196f3;
  --navy:#0d2a6e;
  --ink:#1d1d1d;
  --text:#333;
  --muted:#777;
  --grey-light:#e9e9e9;
  --grey-mid:#8a8a8a;
  --nav-dark:#0f1418;
  --footer:#4a4a4a;
  --red:#d0021b;
  --white:#fff;
}
*{box-sizing:border-box;margin:0;padding:0}
html,body{width:1200px;height:3656px;overflow:hidden}
body{font-family:"Roboto",Arial,sans-serif;color:var(--text);background:var(--white);position:relative}
section,header,footer{position:absolute;left:0;width:1200px}
.abs{position:absolute}
.cond{font-family:"Roboto Condensed","Arial Narrow",sans-serif}

/* top bar */
.topbar{top:0;height:80px;background:var(--white);border-top:6px solid var(--blue)}
.topbar-item{position:absolute;top:22px;font-size:20px;color:var(--text);display:flex;align-items:center;gap:10px}
/* nav */
.navbar{top:80px;height:72px;background:var(--nav-dark)}
.brand{position:absolute;left:20px;top:13px;display:flex;align-items:center;gap:12px;color:var(--white);font-size:40px;font-weight:500;line-height:46px}
.brand-dot{width:44px;height:44px;border-radius:50%;background:var(--blue)}
.nav-right{position:absolute;right:24px;top:18px;display:flex;align-items:center;gap:18px;color:var(--white);font-size:26px}
.nav-right .login{font-size:19px}
.nav-right .sep{color:#aaa;font-size:20px}
.menu-btn{width:38px;height:38px;background:#d6d6d6;border-radius:3px;padding:9px 7px;display:flex;flex-direction:column;justify-content:space-between}
.menu-btn span{height:3px;background:#666}
/* hero */
.hero{top:152px;height:708px;overflow:hidden}
.hero-photo{position:absolute;inset:0;background:linear-gradient(120deg,#3a3a3a 0%,#8d8d8d 35%,#d9d9d9 60%,#bdbdbd 100%)}
.hero-circle{position:absolute;left:596px;top:97px;width:528px;height:528px;border-radius:50%;background:var(--white);text-align:center;padding-top:62px}
.hero-circle h1{font-family:"Roboto Condensed",sans-serif;font-size:48px;line-height:54px;color:var(--ink);font-weight:400}
.hero-circle h1 span{display:block;color:var(--blue)}
.hero-circle .member{font-size:30px;margin-top:18px;color:var(--ink)}
.hero-circle .from{font-size:23px;font-weight:700;margin-top:10px;color:var(--ink)}
.hero-circle .price{font-size:42px;font-weight:700;color:var(--blue);margin-top:4px}
.hero-circle .price small{font-size:24px}
.btn-dark{display:inline-block;margin-top:26px;background:#2a2a2a;color:var(--blue-bright);font-size:26px;font-weight:500;padding:14px 30px;border-radius:3px}
.hero-arrow{position:absolute;left:40px;top:310px}
.dots{position:absolute;left:556px;top:640px;display:flex;gap:14px}
.dots span{width:12px;height:12px;border-radius:50%;background:#333}
.dots span:first-child{background:var(--white)}
.hero-band{top:860px;height:12px;background:#ddd}
.hero-band i{position:absolute;left:0;top:0;height:12px;width:660px;background:var(--blue);clip-path:polygon(0 0,100% 0,97% 100%,0 100%)}
/* call us */
.callus{top:872px;height:595px;background:var(--grey-light);text-align:center}
.callus h2{font-family:"Roboto Condensed",sans-serif;font-size:40px;font-weight:700;color:var(--ink);margin-top:38px}
.callus h3{font-size:28px;font-weight:700;color:var(--blue);margin-top:2px}
.callus p{font-size:21px;color:var(--ink);margin:22px auto 0;width:600px;line-height:28px}
.video{position:absolute;left:286px;top:196px;width:628px;height:354px;background:var(--white);border:2px solid #cfcfcf;overflow:hidden}
.video-brand{position:absolute;left:56px;top:16px;display:flex;align-items:center;gap:14px;font-size:64px;color:var(--blue);font-weight:400}
.video-brand i{width:80px;height:80px;border-radius:50%;background:var(--blue)}
.video-scene{position:absolute;left:40px;top:110px;width:548px;height:196px;background:linear-gradient(180deg,#f4f7fa,#dfe8ee);border-radius:4px}
.video-bar{position:absolute;left:0;bottom:0;width:100%;height:38px;background:rgba(20,20,20,.85);display:flex;align-items:center;padding:0 10px;gap:12px}
.video-bar .pause{width:28px;height:24px;background:#555;display:flex;justify-content:center;align-items:center;gap:4px}
.video-bar .pause b{width:4px;height:12px;background:#fff}
.video-bar .track{flex:1;height:6px;background:#666}
.video-bar .track i{display:block;width:68%;height:6px;background:var(--blue)}
.video-bar .hd{color:#ccc;font-size:13px;font-weight:700}
/* pricing */
.pricing{top:1467px;height:716px;background:var(--white)}
.pricing h2{position:absolute;width:100%;top:60px;text-align:center;font-family:"Roboto Condensed",sans-serif;font-size:40px;line-height:46px;color:var(--ink);font-weight:700}
.pricing h2 span{display:block;color:var(--blue)}
.plan{position:absolute;text-align:center;background:#e4e4e4}
.plan-head{height:66px;line-height:66px;background:#8c8c8c;color:var(--white);font-size:28px;font-family:"Roboto Condensed",sans-serif;font-weight:700}
.plan-price{font-size:50px;font-weight:700;color:var(--ink);margin-top:20px;line-height:56px;font-family:"Roboto Condensed",sans-serif}
.plan-price sup{font-size:28px;vertical-align:14px}
.plan-price small{font-size:30px;color:var(--red)}
.plan-fee{font-size:16px;color:var(--text)}
.plan-box{margin:18px auto 0;width:260px;background:#f4f4f4;border:1px solid #cfcfcf;border-radius:10px;padding:16px 8px;font-size:15px;line-height:19px;color:var(--ink)}
.plan-box strong{display:block;font-size:22px;line-height:26px;font-weight:500}
.btn-navy{display:inline-block;background:var(--navy);color:var(--white);font-size:18px;padding:13px 16px;margin-top:36px}
.plan-premium{left:130px;top:263px;width:315px;height:391px}
.plan-plus{left:762px;top:263px;width:316px;height:391px}
.plan-platinum{left:445px;top:195px;width:317px;height:459px;background:var(--blue-bright)}
.plan-platinum .plan-head{background:var(--navy);height:64px;line-height:64px;font-size:30px}
.plan-platinum .plan-price,.plan-platinum .plan-fee{color:var(--ink)}
.plan-platinum .plan-box{background:#6fb6f7;border-color:#b7dcfc;width:262px}
.plan-platinum .plan-box strong{font-size:20px;line-height:24px}
.popular{position:absolute;left:-4px;top:-22px;width:64px;height:64px;border-radius:50%;background:var(--blue);border:3px solid #cfe6fc;color:var(--white);font-size:11px;font-weight:700;line-height:58px;text-align:center}
/* how it works + features */
.how{top:2183px;height:623px}
.how-left{position:absolute;left:0;top:0;width:599px;height:623px;background:#e6e6e6}
.how-left h2{position:absolute;left:0;width:599px;top:46px;text-align:center;font-size:38px;font-weight:300;color:#333;font-family:"Roboto Condensed",sans-serif}
.step{position:absolute;left:30px;width:550px;height:112px;background:var(--white);padding:12px 110px 0 8px}
.step h3{font-size:28px;font-weight:500;color:var(--ink)}
.step h3 em{font-style:normal;color:var(--blue)}
.step p{font-size:18px;line-height:23px;color:var(--muted);margin-top:2px}
.step svg{position:absolute;right:18px;top:18px}
.btn-blue{position:absolute;left:34px;top:521px;width:226px;height:49px;line-height:49px;text-align:center;background:var(--blue-bright);color:var(--white);font-size:26px;font-weight:500}
.how-right{position:absolute;left:599px;top:0;width:601px;height:623px;background:linear-gradient(135deg,#f7f7f7 0%,#dde6ec 55%,#c9d3da 100%)}
.how-right h2{position:absolute;left:0;width:601px;top:28px;text-align:center;font-family:"Roboto Condensed",sans-serif;font-size:40px;line-height:46px;font-weight:700;color:var(--ink)}
.how-right h2 span{display:block;color:var(--blue)}
.features{position:absolute;left:178px;list-style:none}
.features li{display:flex;align-items:center;gap:18px;font-size:25px;color:var(--ink);height:47px}
/* real-time */
.realtime{top:2806px;height:508px;background:linear-gradient(90deg,#0f6fd6 0%,#1e88e5 60%,#2a93ef 100%);overflow:hidden}
.realtime-photo{position:absolute;left:0;top:0;width:710px;height:508px;background:linear-gradient(90deg,#e9edf1 0%,#c9d6e2 45%,rgba(30,136,229,0) 100%)}
.realtime h2{position:absolute;left:560px;width:500px;top:68px;text-align:center;font-family:"Roboto Condensed",sans-serif;font-size:40px;line-height:48px;font-weight:700;color:var(--ink)}
.realtime h2 span{display:block;color:var(--ink)}
.realtime h2 b{color:var(--white)}
.benefits{position:absolute;left:640px;top:202px;list-style:none}
.benefits li{display:flex;align-items:center;gap:16px;font-size:25px;color:var(--white);height:49px}
/* footer */
.footer{top:3314px;height:293px;background:var(--footer);color:var(--white)}
.footer::before{content:"";position:absolute;left:0;top:0;width:720px;height:6px;background:var(--blue);clip-path:polygon(0 0,100% 0,98% 100%,0 100%)}
.fcol{position:absolute;top:50px}
.fcol h4{font-size:21px;font-weight:500;letter-spacing:.5px;padding-bottom:8px;border-bottom:1px solid #777}
.fcol p{font-size:15px;line-height:19px;margin-top:10px;color:#eee}
.email-field{display:flex;margin-top:24px}
.email-field span{width:200px;height:34px;background:var(--white);color:#888;font-size:15px;padding:8px}
.email-field b{width:42px;height:34px;background:var(--blue);color:var(--white);text-align:center;line-height:34px;font-size:20px}
.links{list-style:none;margin-top:6px}
.links li{font-size:15px;line-height:30px;padding-left:18px;position:relative}
.links li::before{content:"";position:absolute;left:2px;top:13px;width:5px;height:5px;border-radius:50%;background:var(--white)}
.badge{background:#d8d8d8;margin:12px auto 0}
.social{display:flex;gap:16px;margin-top:14px}
.social i{width:30px;height:30px;border-radius:50%;background:var(--white)}
.fphone{font-size:22px;margin-top:20px}
.copy{top:3607px;height:49px;background:var(--blue-bright);color:var(--white);font-size:14px;text-align:center;line-height:49px}
</style>
</head>
<body>

<header class="topbar">
  <div class="topbar-item" style="left:720px">
    <svg width="26" height="18" viewBox="0 0 26 18"><rect x="1" y="1" width="24" height="16" fill="none" stroke="#666" stroke-width="2"/><path d="M1 1l12 9 12-9" fill="none" stroke="#666" stroke-width="2"/></svg>
    info@brightdesk.com
  </div>
  <div class="topbar-item" style="left:980px">
    <svg width="30" height="18" viewBox="0 0 30 18"><path d="M2 6h8l3 5-4 6H4zM14 2h12l2 6-6 8-6-6z" fill="#999"/></svg>
    United States - EN
  </div>
</header>

<header class="navbar">
  <div class="brand"><span class="brand-dot"></span>brightdesk</div>
  <div class="nav-right">
    <svg width="28" height="28" viewBox="0 0 24 24"><path d="M6.6 10.8a15 15 0 0 0 6.6 6.6l2.2-2.2a1 1 0 0 1 1-.25 11.4 11.4 0 0 0 3.6.57 1 1 0 0 1 1 1V20a1 1 0 0 1-1 1A17 17 0 0 1 3 4a1 1 0 0 1 1-1h3.5a1 1 0 0 1 1 1c0 1.25.2 2.45.57 3.57a1 1 0 0 1-.25 1z" fill="#fff"/></svg>
    <span>(888) 555-0142</span>
    <span class="sep">|</span><span class="login">Login</span><span class="sep">|</span>
    <div class="menu-btn"><span></span><span></span><span></span></div>
  </div>
</header>

<section class="hero">
  <div class="hero-photo" role="img" aria-label="Black and white photo of hands typing on a laptop showing the Brightdesk website"></div>
  <svg class="hero-arrow" width="24" height="44" viewBox="0 0 24 44"><path d="M20 2L4 22l16 20" fill="none" stroke="#bbb" stroke-width="3"/></svg>
  <div class="hero-circle">
    <h1>Dedicated Support<span>Anytime Anywhere</span></h1>
    <div class="member">Become a Member Today!</div>
    <div class="from">Starting At Only</div>
    <div class="price">$19.99<small>/mo</small></div>
    <span class="btn-dark">Get Help Now!</span>
  </div>
  <div class="dots"><span></span><span></span><span></span><span></span></div>
</section>
<div class="abs hero-band" style="left:0;width:1200px"><i></i></div>

<section class="callus">
  <h2>CALL US TODAY</h2>
  <h3>And get started with our dedicated technicians.</h3>
  <p>Get a 30-minute one-on-one free consultation with one of our experts! •</p>
  <div class="video">
    <div class="video-brand"><i></i>brightdesk</div>
    <div class="video-scene" role="img" aria-label="Cartoon of two support technicians standing beside a computer tower and monitor"></div>
    <div class="video-bar"><span class="pause"><b></b><b></b></span><span class="track"><i></i></span><span class="hd">HD</span></div>
  </div>
</section>

<section class="pricing">
  <h2>MEMBERSHIP PRICING<span>AND PLANS</span></h2>

  <div class="plan plan-premium">
    <div class="plan-head">PREMIUM</div>
    <div class="plan-price"><sup>$</sup>19.99<small>/mo</small></div>
    <div class="plan-fee">($249-$300 setup fee)</div>
    <div class="plan-box">Regular 90-Day Optimization<br>Unlimited 24/7 Tier 3<strong>Technician Support</strong></div>
    <span class="btn-navy">LEARN MORE</span>
  </div>

  <div class="plan plan-platinum">
    <span class="popular">POPULAR</span>
    <div class="plan-head">PLATINUM</div>
    <div class="plan-price"><sup>$</sup>39.99<small>/mo</small></div>
    <div class="plan-fee">($249-$300 setup fee)</div>
    <div class="plan-box">Regular 90-Day Optimization<br>Unlimited 24/7 Tier 3<br>Technician Support<strong>Online Identity Theft Protection</strong></div>
    <span class="btn-navy" style="margin-top:28px">LEARN MORE</span>
  </div>

  <div class="plan plan-plus">
    <div class="plan-head">PREMIUM PLUS</div>
    <div class="plan-price"><sup>$</sup>29.99<small>/mo</small></div>
    <div class="plan-fee">($249-$300 setup fee)</div>
    <div class="plan-box">Regular 90-Day Optimization<br>Unlimited 24/7 Tier 3<strong>Technician Support</strong></div>
    <span class="btn-navy">LEARN MORE</span>
  </div>
</section>

<section class="how">
  <div class="how-left">
    <h2>HOW IT WORKS</h2>
    <div class="step" style="top:124px">
      <h3><em>FREE</em> Diagnostic</h3>
      <p>Get a diagnostic, FOR FREE! Get a free consultation with our staff.</p>
      <svg width="86" height="70" viewBox="0 0 86 70"><path d="M2 38h22l8-30 12 56 10-40 6 14h22" fill="none" stroke="var(--blue)" stroke-width="4" stroke-linejoin="round"/><circle cx="80" cy="38" r="4" fill="var(--blue)"/></svg>
    </div>
    <div class="step" style="top:248px">
      <h3><em>Get</em> Fixed</h3>
      <p>Get fixed, IMMEDIATELY! Our staff will solve your computer issues right before your eyes.</p>
      <svg width="70" height="74" viewBox="0 0 70 74"><path d="M6 32h14v36H6zM24 34l12-26c6 0 8 4 7 10l-3 12h20c4 0 6 4 4 8l-7 26c-1 3-3 4-6 4H24z" fill="none" stroke="#333" stroke-width="4" stroke-linejoin="round"/></svg>
    </div>
    <div class="step" style="top:372px">
      <h3><em>Backup your</em> information!</h3>
      <p>Saving your files is now EASY! You will be able to retain your personal files without any loss of data.</p>
      <svg width="76" height="78" viewBox="0 0 76 78"><ellipse cx="28" cy="10" rx="26" ry="8" fill="var(--blue)"/><path d="M2 14v14c0 5 12 8 26 8s26-3 26-8V14c0 5-12 8-26 8S2 19 2 14zM2 32v14c0 5 12 8 26 8s26-3 26-8V32c0 5-12 8-26 8S2 37 2 32zM2 50v14c0 5 12 8 26 8V58c-14 0-26-3-26-8z" fill="var(--blue)"/><path d="M60 40v22M50 54l10 12 10-12" fill="none" stroke="var(--blue)" stroke-width="6"/></svg>
    </div>
    <span class="btn-blue">Know More</span>
  </div>
  <div class="how-right" role="img" aria-label="Soft photo of a laptop, tablet and coffee cup on a bright desk">
    <h2>ALL THE BEST FEATURES,<span>AT THE BEST PRICE!</span></h2>
    <ul class="features" style="top:165px">
      <li><svg width="22" height="18" viewBox="0 0 22 18"><path d="M2 9l6 6L20 2" fill="none" stroke="#222" stroke-width="4"/></svg>Ad Blocker</li>
      <li><svg width="22" height="18" viewBox="0 0 22 18"><path d="M2 9l6 6L20 2" fill="none" stroke="#222" stroke-width="4"/></svg>Regular Tune-Ups</li>
      <li><svg width="22" height="18" viewBox="0 0 22 18"><path d="M2 9l6 6L20 2" fill="none" stroke="#222" stroke-width="4"/></svg>System Reports</li>
      <li><svg width="22" height="18" viewBox="0 0 22 18"><path d="M2 9l6 6L20 2" fill="none" stroke="#222" stroke-width="4"/></svg>Multiple Devices</li>
    </ul>
    <ul class="features" style="top:370px">
      <li><svg width="22" height="18" viewBox="0 0 22 18"><path d="M2 9l6 6L20 2" fill="none" stroke="#222" stroke-width="4"/></svg>Identity Protection</li>
      <li><svg width="22" height="18" viewBox="0 0 22 18"><path d="M2 9l6 6L20 2" fill="none" stroke="#222" stroke-width="4"/></svg>Mobile Security</li>
      <li><svg width="22" height="18" viewBox="0 0 22 18"><path d="M2 9l6 6L20 2" fill="none" stroke="#222" stroke-width="4"/></svg>Cross Platform Support</li>
      <li><svg width="22" height="18" viewBox="0 0 22 18"><path d="M2 9l6 6L20 2" fill="none" stroke="#222" stroke-width="4"/></svg>Cloud Backup</li>
    </ul>
  </div>
</section>

<section class="realtime">
  <div class="realtime-photo" role="img" aria-label="Photo of support agents wearing headsets in a call centre"></div>
  <h2>Real-Time Support<span>Features and <b>BENEFITS</b></span></h2>
  <ul class="benefits">
    <li><svg width="24" height="20" viewBox="0 0 24 20"><path d="M2 10l7 7L22 2" fill="none" stroke="#fff" stroke-width="4"/></svg>24/7 Real-Time Technician Support</li>
    <li><svg width="24" height="20" viewBox="0 0 24 20"><path d="M2 10l7 7L22 2" fill="none" stroke="#fff" stroke-width="4"/></svg>The best Security Software in the market</li>
    <li><svg width="24" height="20" viewBox="0 0 24 20"><path d="M2 10l7 7L22 2" fill="none" stroke="#fff" stroke-width="4"/></svg>Regular tune-ups and optimization</li>
    <li><svg width="24" height="20" viewBox="0 0 24 20"><path d="M2 10l7 7L22 2" fill="none" stroke="#fff" stroke-width="4"/></svg>Setup and installation included</li>
  </ul>
</section>

<footer class="footer">
  <div class="fcol" style="left:117px;width:250px">
    <h4>NEWSLETTER SIGNUP</h4>
    <p>Sign up for our regular informational newsletters</p>
    <div class="email-field"><span>e-mail</span><b>»</b></div>
  </div>
  <div class="fcol" style="left:435px;width:170px">
    <h4>TOP LINKS</h4>
    <ul class="links"><li>Home</li><li>About Us</li><li>Services</li><li>Contact Us</li><li>FAQs</li></ul>
  </div>
  <div class="fcol" style="left:680px;width:165px;text-align:center">
    <h4>TRUSTED BY</h4>
    <div class="badge" style="width:110px;height:40px"></div>
    <div class="badge" style="width:56px;height:56px;border-radius:50%"></div>
    <div class="badge" style="width:56px;height:64px;border-radius:6px"></div>
  </div>
  <div class="fcol" style="left:904px;width:180px">
    <h4>FOLLOW US</h4>
    <div class="social"><i></i><i></i><i></i></div>
    <div class="fphone">(888) 555-0142</div>
  </div>
</footer>
<div class="abs copy" style="left:0;width:1200px">Brightdesk © 2016. All rights reserved. Terms and Conditions - Refund Policy - Privacy Policy.</div>

</body>
</html>
```